Business Card Design Project

Hello Designers, hope you are all aiming enjoy the weekend
I have the Business Logo (uploaded), you can alter the color which ever way you think would work,
Im looking for a simple yet striking feel, something which will stay memorable (I have uploaded 3 examples for you to flick through)
Information on the card, will just be the bare minimum,
Double Sided
Info being
i.e.
Name
Number
Website
ABN
Tobin Wexmoor
+468213579 (singapore)
+315792846 (Australia)
+729384615 (America)
www.lomevu-linkup.example
ABN 86420913
Enjoy,
Tobin
Industry/Entity Type
Business
Look and feel
Each slider illustrates characteristics of the customer's brand and the style your logo design should communicate.

```html
<!DOCTYPE html>
<html lang="en">
<head>
<meta charset="utf-8">
<title>Lomevu Linkup — Business Card</title>
<link rel="stylesheet" href="https://fonts.googleapis.com/css2?family=Montserrat:wght@400;500;600&display=swap">
<style>
  :root {
    --page: #ffffff;
    --kraft: #c8a66c;
    --kraft-edge: #b8965c;
    --ink-white: #ffffff;
  }
  * { margin: 0; padding: 0; box-sizing: border-box; }
  html, body {
    width: 1200px;
    height: 1200px;
    overflow: hidden;
    background: var(--page);
    font-family: "Montserrat", Arial, sans-serif;
  }
  .canvas {
    position: relative;
    width: 1200px;
    height: 1200px;
  }
  .card {
    position: absolute;
    left: 220px;
    width: 760px;
    height: 420px;
  }
  .card--front { top: 140px; }
  .card--back  { top: 640px; }
  .card__shape {
    position: absolute;
    inset: 0;
    width: 760px;
    height: 420px;
  }
  .card__stock { fill: var(--kraft); stroke: var(--kraft-edge); stroke-width: 1; }
  .card__band  { fill: var(--ink-white); }

  .brand-name {
    position: absolute;
    left: 120px;
    top: 178px;
    font-size: 46px;
    font-weight: 500;
    color: var(--ink-white);
    letter-spacing: 0.5px;
    line-height: 64px;
  }

  .contact {
    position: absolute;
    right: 110px;
    top: 104px;
    text-align: right;
    color: var(--ink-white);
  }
  .contact__name {
    font-size: 22px;
    font-weight: 600;
    letter-spacing: 3px;
    text-transform: uppercase;
    margin-bottom: 16px;
  }
  .contact__line {
    font-size: 16px;
    font-weight: 400;
    letter-spacing: 1.5px;
    line-height: 22px;
    text-transform: uppercase;
  }
</style>
</head>
<body>
<main class="canvas">

  <section class="card card--front" aria-label="Business card front">
    <svg class="card__shape" viewBox="0 0 760 420" aria-hidden="true">
      <path class="card__stock" d="M0,0 H550 A210,210 0 0 1 550,420 H0 Z"/>
      <path class="card__band" d="M0,22 H550 A188,188 0 0 1 550,398 H110 V358 H550 A148,148 0 0 0 550,62 H0 Z"/>
    </svg>
    <p class="brand-name">Lomevu Linkup</p>
  </section>

  <section class="card card--back" aria-label="Business card back">
    <svg class="card__shape" viewBox="0 0 760 420" aria-hidden="true">
      <g transform="translate(760,0) scale(-1,1)">
        <path class="card__stock" d="M0,0 H550 A210,210 0 0 1 550,420 H0 Z"/>
        <path class="card__band" d="M0,22 H550 A188,188 0 0 1 550,398 H110 V358 H550 A148,148 0 0 0 550,62 H0 Z"/>
      </g>
    </svg>
    <div class="contact">
      <p class="contact__name">Tobin Wexmoor</p>
      <p class="contact__line">+468213579 (Singapore)</p>
      <p class="contact__line">+315792846 (Australia)</p>
      <p class="contact__line">+729384615 (America)</p>
      <p class="contact__line">www.lomevu-linkup.example</p>
      <p class="contact__line">ABN 86420913</p>
    </div>
  </section>

</main>
</body>
</html>
```